Ridgeline Outfitters Business Cards

Recently had a logo done with Artfolio and now looking for a business card to go along with it.

Target Market(s)

Ridgeline Outfitters is a weapons dealer. My market will be primarily men, hunting, shooting type.

Industry/Entity Type

Business

Contact Information for Business Card

I selected double sided, but this is not required, single or double is going to be fine. I picture the logo on one side, or perhaps just the circle which contains "RO" with the remaining info on the other side.

Font styles to use
Sans Serif

Requirements
Must have
• My name: Milo Brandt
• Title: Owner
• tel: 612-555-0187
• web: www.ridgelineoutfittersmn.example
Nice to have
• I like the concept of a black business card. I would like to keep the colors monotone, black, grey, white or red. Red is acceptable because it is in the logo. I have also seen cards that are matte black with shiny black as well, perhaps for the logo (or circle RO) part of the logo.
• I will upload a couple of the logos for use, and also an example I just found of the black on black. and some others that have a nice contrast.
Should not have
• lots of colors are not wanted.

```html
<!DOCTYPE html>
<html lang="en">
<head>
<meta charset="utf-8">
<title>Ridgeline Outfitters Business Cards</title>
<link href="https://fonts.googleapis.com/css2?family=Abel&family=Oswald:wght@500;600&display=swap" rel="stylesheet">
<style>
  :root {
    --page: #e6e2dc;
    --card-black: #000000;
    --steel-grey: #777777;
    --signal-red: #e01f26;
    --white: #ffffff;
    --edge: #cfcfcf;
  }
  * { box-sizing: border-box; margin: 0; padding: 0; }
  html, body { width: 1036px; height: 1200px; overflow: hidden; }
  body { background: var(--page); position: relative; }

  .card {
    position: absolute;
    width: 778px;
    height: 450px;
    background: var(--card-black);
    border: 1px solid var(--edge);
    overflow: hidden;
  }
  .card--front { left: 125px; top: 118px; }
  .card--back  { left: 133px; top: 627px; }

  .front-panel { position: absolute; inset: 0; }

  .wordmark {
    position: absolute;
    left: 330px;
    top: 187px;
    width: 420px;
    text-align: center;
    font-family: "Oswald", sans-serif;
    font-weight: 600;
    font-size: 36px;
    letter-spacing: 2px;
    text-transform: uppercase;
    color: var(--signal-red);
    line-height: 1;
  }

  .contact {
    position: absolute;
    left: 100px;
    top: 116px;
    color: var(--white);
  }
  .contact__name {
    font-family: "Oswald", sans-serif;
    font-weight: 600;
    font-size: 26px;
    line-height: 32px;
  }
  .contact__title {
    font-family: "Abel", sans-serif;
    font-size: 26px;
    line-height: 32px;
    margin-bottom: 20px;
  }
  .contact__list { list-style: none; }
  .contact__item {
    display: flex;
    align-items: center;
    gap: 14px;
    font-family: "Abel", sans-serif;
    font-size: 25px;
    height: 40px;
  }
  .contact__icon { width: 24px; height: 24px; flex: none; }

  .back-mark { position: absolute; left: 546px; top: 62px; }
</style>
</head>
<body>
  <section class="card card--front" aria-label="Card front">
    <svg class="front-panel" width="778" height="450" viewBox="0 0 778 450">
      <circle cx="77" cy="225" r="226" fill="var(--steel-grey)" stroke="var(--signal-red)" stroke-width="3"/>
      <circle class="front-panel__ring" cx="138" cy="208" r="92" fill="none" stroke="var(--card-black)" stroke-width="9"/>
    </svg>
    <div class="wordmark">Ridgeline Outfitters</div>
  </section>

  <section class="card card--back" aria-label="Card back">
    <div class="contact">
      <p class="contact__name">Milo Brandt</p>
      <p class="contact__title">Owner</p>
      <ul class="contact__list">
        <li class="contact__item">
          <svg class="contact__icon" viewBox="0 0 24 24" aria-hidden="true">
            <rect x="6" y="1.5" width="12" height="21" rx="2" fill="none" stroke="var(--signal-red)" stroke-width="2"/>
            <line x1="6" y1="18" x2="18" y2="18" stroke="var(--signal-red)" stroke-width="1.5"/>
          </svg>
          612-555-0187
        </li>
        <li class="contact__item">
          <svg class="contact__icon" viewBox="0 0 24 24" aria-hidden="true">
            <rect x="1.5" y="5" width="21" height="14" fill="none" stroke="var(--signal-red)" stroke-width="2"/>
            <polyline points="1.5,5 12,13 22.5,5" fill="none" stroke="var(--signal-red)" stroke-width="2"/>
          </svg>
          milo@ridgelineoutfittersmn.example
        </li>
        <li class="contact__item">
          <svg class="contact__icon" viewBox="0 0 24 24" aria-hidden="true">
            <circle cx="12" cy="12" r="10" fill="none" stroke="var(--signal-red)" stroke-width="2"/>
            <ellipse cx="12" cy="12" rx="4.5" ry="10" fill="none" stroke="var(--signal-red)" stroke-width="1.5"/>
            <line x1="2" y1="12" x2="22" y2="12" stroke="var(--signal-red)" stroke-width="1.5"/>
          </svg>
          www.ridgelineoutfittersmn.example
        </li>
      </ul>
    </div>
    <svg class="back-mark" width="172" height="172" viewBox="0 0 172 172" aria-hidden="true">
      <circle cx="86" cy="86" r="80" fill="none" stroke="var(--steel-grey)" stroke-width="9"/>
    </svg>
  </section>
</body>
</html>
```